Maple Ridge business card design

Card needs to include the following text/items:
Company Logo
Tobin Marsh
Phone # - 555-318-7642
service@mapleridgelandscaping.example
Lawn & landscape maintenance services

```html
<!DOCTYPE html>
<html lang="en">
<head>
<meta charset="utf-8">
<title>Maple Ridge Business Card</title>
<link rel="stylesheet" href="https://fonts.googleapis.com/css2?family=Cinzel:wght@700&family=Open+Sans:wght@400;700&display=swap">
<style>
  :root {
    --bg: #dcdcdc;
    --card: #ffffff;
    --forest: #1d4a2a;
    --leaf: #8aa83f;
    --ink: #3a3a3a;
    --sky-top: #1bc1f1;
    --sky-mid: #7fd4f3;
    --sky-low: #e6f6fb;
    --hill-edge: #24513a;
    --hill: #042b18;
    --meadow: #7d9e42;
  }
  * { box-sizing: border-box; margin: 0; padding: 0; }
  html, body { width: 1074px; height: 1200px; overflow: hidden; }
  body {
    background: var(--bg);
    font-family: "Open Sans", sans-serif;
    position: relative;
  }
  .card {
    position: absolute;
    top: 466px;
    width: 470px;
    height: 268px;
    background: var(--card);
    box-shadow: 0 6px 16px rgba(0,0,0,0.18);
    overflow: hidden;
  }
  .card--front { left: 47px; }
  .card--back { left: 557px; }

  /* wordmark: one colour, one weight */
  .wordmark {
    font-family: "Cinzel", serif;
    font-weight: 700;
    color: var(--forest);
    text-align: center;
    white-space: nowrap;
  }
  .wordmark__name { display: block; line-height: 1; }
  .wordmark__sub { display: block; line-height: 1; }

  .brand {
    position: absolute;
    left: 18px;
    top: 42px;
    width: 166px;
  }
  .brand__mark {
    display: block;
    width: 108px;
    height: 108px;
    margin: 0 auto 6px;
    border-radius: 50%;
    border: 2px solid var(--leaf);
  }
  .brand .wordmark__name { font-size: 21px; }
  .brand .wordmark__sub {
    font-size: 9px;
    letter-spacing: 6.6px;
    padding-left: 6.6px;
    margin-top: 3px;
  }

  .person {
    position: absolute;
    left: 210px;
    top: 54px;
  }
  .person__name {
    font-family: "Cinzel", serif;
    font-weight: 700;
    font-size: 23px;
    color: var(--forest);
    line-height: 1;
    margin-bottom: 16px;
  }
  .contact { list-style: none; }
  .contact li {
    display: flex;
    align-items: center;
    font-size: 12px;
    line-height: 16px;
    color: var(--ink);
  }
  .contact svg { width: 9px; height: 9px; margin-right: 6px; fill: var(--ink); flex: none; }
  .contact .social { margin-top: 12px; }
  .social__dot {
    width: 13px; height: 13px; border-radius: 50%;
    background: var(--leaf); margin-right: 4px; flex: none;
  }

  .tagline {
    position: absolute;
    left: 0; right: 0;
    top: 218px;
    height: 22px;
    background: var(--leaf);
    color: #fff;
    font-weight: 700;
    font-size: 11.5px;
    letter-spacing: 0.6px;
    text-align: center;
    line-height: 22px;
    text-transform: uppercase;
  }

  .scene {
    position: absolute; inset: 0;
    background: linear-gradient(180deg,
      var(--sky-top) 0%,
      var(--sky-mid) 30%,
      var(--sky-low) 56%,
      var(--hill-edge) 64%,
      var(--hill) 72%,
      var(--hill) 82%,
      var(--meadow) 94%,
      var(--meadow) 100%);
  }
  .back__brand {
    position: absolute;
    left: 0; right: 0; top: 22px;
  }
  .back__brand .wordmark__name { font-size: 44px; }
  .back__brand .wordmark__sub {
    font-size: 16px;
    letter-spacing: 14.5px;
    padding-left: 14.5px;
    margin-top: 6px;
  }
</style>
</head>
<body>
  <section class="card card--front">
    <div class="brand">
      <span class="brand__mark"></span>
      <div class="wordmark">
        <span class="wordmark__name">Maple Ridge</span>
        <span class="wordmark__sub">LANDSCAPING</span>
      </div>
    </div>

    <div class="person">
      <h1 class="person__name">Tobin Marsh</h1>
      <ul class="contact">
        <li><svg viewBox="0 0 10 10" aria-hidden="true"><path d="M2 0.5 L3.6 0.5 L4.2 2.8 L3.1 3.6 Q4 5.8 6.3 6.9 L7.2 5.8 L9.5 6.4 L9.5 8 Q9.5 9.5 8 9.5 Q0.5 9 0.5 2 Q0.5 0.5 2 0.5Z"/></svg>555-318-7642</li>
        <li><svg viewBox="0 0 10 10" aria-hidden="true"><path d="M0 2 H10 V8.5 H0Z M0.6 2.4 L5 5.8 L9.4 2.4" stroke="#fff" stroke-width="0.8"/></svg>service@mapleridgelandscaping.example</li>
        <li><svg viewBox="0 0 10 10" aria-hidden="true"><circle cx="5" cy="5" r="4.5"/><path d="M0.5 5 H9.5 M5 0.5 V9.5" stroke="#fff" stroke-width="0.7"/></svg>mapleridgelandscaping.example</li>
        <li class="social"><span class="social__dot"></span>mapleridgelandscaping</li>
      </ul>
    </div>

    <div class="tagline">Lawn &amp; Landscape Maintenance Services</div>
  </section>

  <section class="card card--back">
    <div class="scene" role="img" aria-label="Illustrated countryside: blue sky, setting sun, dark green hills, a bare tree and a leafy tree beside a white fence and path"></div>
    <div class="back__brand wordmark">
      <span class="wordmark__name">Maple Ridge</span>
      <span class="wordmark__sub">LANDSCAPING</span>
    </div>
  </section>
</body>
</html>
```